Local Newspaper Quarterly " Meet The Realtor" print ad

I need a new add made up. This was my last ad:
http://www.harborlinepressads.example/static/pdfs/agents1309/Ar092213%20G10%20006%20Prepress.pdf

I do not really care of Realtor advertisements because they are just so cheesy and rather pompous-like. However, it's a necessary evil
My ads have always been outside of the box and/or visually sharp.
I now have a new company' Voske Real Estate( I will attach a logo) contact info:
Carl Voske
Voske Real Estate
Broker/Owner( this can be somewhere in small print or corner of ad since it's mandatory to have shown
Phone: 304-555-0194
Email: Carl@VoskeRealEstate.Example
VoskeRealEstate.Example
I would like social icons(FL,Chirpr, Pinmosaic! Dwello, Qlink)

Ideas: In my logo font or using the image at the top I envision
Something like:
A
Voske Real Estate
Of Mind
Body of ad?
Images of Charleston WV as a real light back ground
With 3 or 4 customer reviews chosen by you in this site:
http://webcarl.example/think.html

Bottom: contact info and my name in a nice Signature style ??
My agent pic at the bottom right( to be small. I don't want my big head overshadowing the message)

I have yet to think of a tagline for my new company:
I have been thinking of " Luxury Services For All Things Real Estate"

Or nothing at all ??? I don't care for tag lines but then again that's part of the business

Target Market(s)

Higher end homes

Industry/Entity Type

Business

Colors
0f59a5
0392cd
0f0f0f
eaeaea
ffffff

Requirements
Must have
• My logo and colors
Nice to have
• My agent picture and client review.
Should not have
• No typical real estate images like a house or home buyer

```html
<!DOCTYPE html>
<html lang="en">
<head>
<meta charset="utf-8">
<title>Voske Real Estate – Meet the Realtor</title>
<link href="https://fonts.googleapis.com/css2?family=Jost:ital,wght@0,300;0,400;0,700;1,400&display=swap" rel="stylesheet">
<style>
  :root {
    --brand-blue: #1470b9;
    --band-dark: #3a3d40;
    --white: #ffffff;
    --paper: #ffffff;
    --tile-grey: #8a8d90;
    --ink: #0f0f0f;
  }
  * { box-sizing: border-box; margin: 0; padding: 0; }
  html, body { width: 1200px; height: 922px; overflow: hidden; background: var(--paper); }
  body { font-family: "Jost", "Futura", sans-serif; position: relative; }

  .ad { position: relative; width: 1200px; height: 922px; overflow: hidden; background: var(--paper); }

  .brand-tile {
    position: absolute; left: 511px; top: 31px; width: 176px; height: 176px;
    background: linear-gradient(135deg, #cfd1d3 0%, #8a8d90 55%, #5f6265 100%);
    display: flex; align-items: center; justify-content: center; text-align: center;
  }
  .brand-tile__name {
    font-weight: 700; font-size: 25px; line-height: 1.1; color: var(--white);
    text-transform: uppercase; letter-spacing: 2px;
  }

  .city-photo {
    position: absolute; left: 0; top: 224px; width: 453px; height: 698px;
    background: linear-gradient(180deg, #c9d9ea 0%, #e8eef4 28%, #8a8f6a 42%, #a99b86 55%, #7f8a8c 68%, #4f6e58 82%, #6a4a3a 100%);
  }

  .panel {
    position: absolute; left: 453px; top: 224px; width: 747px; height: 698px;
    background: var(--brand-blue); color: var(--white);
  }
  .headline { position: absolute; left: 57px; top: 8px; font-weight: 300; }
  .headline__lead { font-size: 74px; line-height: 1; letter-spacing: -0.5px; text-shadow: 1px 2px 4px rgba(0,0,0,.35); }
  .headline__row { display: flex; align-items: flex-end; margin-top: 8px; margin-left: 86px; }
  .headline__small { font-size: 33px; line-height: 1.08; text-align: right; margin-right: 22px; padding-bottom: 4px; }
  .headline__big { font-weight: 400; font-size: 94px; line-height: .92; letter-spacing: -0.5px; text-shadow: 1px 2px 4px rgba(0,0,0,.35); }

  .reviews {
    position: absolute; left: 57px; top: 205px; width: 631px;
    font-weight: 300; font-size: 15.3px; line-height: 19.6px; text-align: justify;
  }
  .reviews__intro { margin-bottom: 20px; }
  .review { margin-bottom: 20px; }
  .review__author { font-style: italic; font-weight: 400; }
  .reviews__cta { font-weight: 400; margin-top: 0; }

  .contact-band {
    position: absolute; left: 0; top: 782px; width: 1200px; height: 100px;
    background: var(--band-dark);
  }
  .social { position: absolute; left: 58px; top: 42px; display: flex; gap: 13px; list-style: none; }
  .social__item {
    width: 42px; height: 42px; background: var(--white); border-radius: 3px;
    display: flex; align-items: center; justify-content: center;
    font-size: 8px; font-weight: 400; color: var(--band-dark);
  }
  .contact {
    position: absolute; right: 215px; top: 8px; text-align: right; color: var(--white);
    font-weight: 300; font-size: 15.5px; line-height: 19px; letter-spacing: .8px;
  }
  .contact__lead { font-weight: 700; font-size: 17.5px; letter-spacing: 1.2px; margin-bottom: 1px; }

  .agent-photo {
    position: absolute; left: 1015px; top: 769px; width: 126px; height: 126px;
    border: 4px solid var(--white);
    background: linear-gradient(160deg, #c98a3a 0%, #8a6a34 45%, #b9c4cf 100%);
  }
</style>
</head>
<body>
<main class="ad">
  <div class="brand-tile"><span class="brand-tile__name">Voske<br>Real Estate</span></div>

  <div class="city-photo" role="img" aria-label="Photo of Charleston, West Virginia: a steel truss bridge over the river leading into the downtown skyline under a cloudy sky"></div>

  <section class="panel">
    <h1 class="headline">
      <span class="headline__lead">Luxury Services</span>
      <span class="headline__row">
        <span class="headline__small">For All<br>Things</span>
        <span class="headline__big">Real Estate</span>
      </span>
    </h1>

    <div class="reviews">
      <p class="reviews__intro">See what the people are saying...</p>
      <p class="review">In trying to buy a home from long distance, Carl went above and beyond his duty as my Realtor. His professionalism, knowledge and attentiveness were absolutely superb! What could have been a nightmare experience, turned out to be a wonderfully smooth transition. Thanks for all your help – it was truly appreciated! A++ <span class="review__author">~ Dana Whitfield</span></p>
      <p class="review">In this difficult sales market, I believe every effort was made to sell our home successfully. We truly appreciate the expenditure of time , energy and resources by Summit Ridge Realty and their encouragement and persistence extended in this successful outcome. <span class="review__author">~ Tom and Lisa Harrow</span></p>
      <p class="review">We have and will recommend Carl Voske to anyone looking to buy or sell any Real Estate. We feel Carl did an exceptional job selling our property even that it was was at the low end of the Real Estate market. <span class="review__author">~ Mark and Jenna Rowley</span></p>
      <p class="reviews__cta">Call me today to book an appointment.</p>
    </div>
  </section>

  <footer class="contact-band">
    <ul class="social" aria-label="Social channels">
      <li class="social__item">FL</li>
      <li class="social__item">Chirpr</li>
      <li class="social__item">Qlink</li>
      <li class="social__item">Pinmosaic</li>
      <li class="social__item">Vidstream</li>
      <li class="social__item">Dwello</li>
    </ul>
    <address class="contact">
      <p class="contact__lead">Carl Voske - For more information call 304-555-0194</p>
      <p>Broker/Owner • Voske Real Estate</p>
      <p>Carl@VoskeRealEstate.Example</p>
      <p>Visit VoskeRealEstate.Example today.</p>
    </address>
  </footer>

  <div class="agent-photo" role="img" aria-label="Portrait of agent Carl Voske outdoors in front of autumn foliage"></div>
</main>
</body>
</html>
```